Wedding and event Photography company.

We need a business card design for a photography company based in Singapore named TamKeza. Our core service offering is wedding photojournalism. We would like to see minimalistic designs that use the colour white. The final design should communicate a sense of ease and reliability.

The attached are a couple of visual reference which i found over the web, i hope it will helps.

Project Brief Update (14th July 2014):
- Please refrain from using any images from the website for the design. The laws and regulations over here does not allow me to distribute my client's images. Thanks!

Target Market(s)

Young and middle aged adults aged 24 - 38. With money to spend =D

Industry/Entity Type

Business

Contact Information for Business Card

Name: Dev Lunor
Designation: Head Photographer
Mobile: +65 81749026
Email: jun@tamkeza.example
Website: www.tamkeza.example

Font styles to use
Other font styles liked:
• Baskerville URW

Colors

Designer to choose colors to be used in the design.

Requirements
Must have
• Must include:
• - The brand TamKeza
• - The logo attached
• - Please help to place the brand TamKeza with the logo according to your preferences.
• - Services
• - Wedding Photography
• - Portraiture
• - Photojournalism
Nice to have
• Looking forward to an elegant and simple design. Please see attached examples!
• Please use Serif Fonts
Should not have
• Please refrain from using dark tones for the majority of the design.
• Please refrain from letterpress and embossing.

```html
<!DOCTYPE html>
<html lang="en">
<head>
<meta charset="utf-8">
<title>TamKeza Business Card</title>
<link rel="stylesheet" href="https://fonts.googleapis.com/css2?family=Roboto:wght@400;700&display=swap">
<style>
  :root {
    --backdrop: #6b7479;
    --card: #ffffff;
    --ink: #111111;
    --ink-soft: #2a2a2a;
    --shadow: rgba(0, 0, 0, 0.35);
  }
  * { margin: 0; padding: 0; box-sizing: border-box; }
  html, body {
    width: 1200px;
    height: 900px;
    overflow: hidden;
    background: var(--backdrop);
    font-family: "Roboto", Arial, sans-serif;
    color: var(--ink);
  }
  .sheet {
    width: 1200px;
    height: 900px;
    display: flex;
    flex-direction: column;
    align-items: center;
    justify-content: center;
    gap: 60px;
  }
  .card {
    position: relative;
    width: 640px;
    height: 366px;
    background: var(--card);
    border-radius: 22px;
    box-shadow: 0 10px 28px var(--shadow);
  }
  .brand-name {
    font-family: "Roboto", Arial, sans-serif;
    font-weight: 700;
    color: var(--ink);
    letter-spacing: 0.5px;
  }

  /* Front: brand only */
  .card-front .brand-name {
    position: absolute;
    left: 0; right: 0;
    top: 140px;
    text-align: center;
    font-size: 58px;
  }
  .card-front .site {
    position: absolute;
    left: 190px;
    top: 252px;
    font-size: 15px;
    font-weight: 700;
    color: var(--ink-soft);
  }

  /* Back: brand + contact */
  .card-back .brand-name {
    position: absolute;
    left: 60px;
    top: 138px;
    width: 230px;
    text-align: center;
    font-size: 40px;
  }
  .card-back .divider {
    position: absolute;
    left: 318px;
    top: 96px;
  }
  .card-back .reg-no {
    position: absolute;
    left: 58px;
    top: 292px;
    width: 240px;
    text-align: center;
    font-size: 14px;
    color: var(--ink-soft);
  }
  .contact {
    position: absolute;
    left: 400px;
    top: 118px;
  }
  .contact-name {
    font-size: 22px;
    font-weight: 700;
    margin: 0 0 16px 34px;
  }
  .contact-list { list-style: none; }
  .contact-list li {
    display: flex;
    align-items: center;
    gap: 12px;
    font-size: 15px;
    line-height: 26px;
    color: var(--ink-soft);
  }
  .contact-list svg { width: 14px; height: 14px; flex: none; }
</style>
</head>
<body>
<main class="sheet">
  <section class="card card-front" aria-label="Card front">
    <div class="brand-name">TamKeza</div>
    <div class="site">www.tamkeza.example</div>
  </section>

  <section class="card card-back" aria-label="Card back">
    <div class="brand-name">TamKeza</div>
    <svg class="divider" width="60" height="150" viewBox="0 0 60 150" aria-hidden="true">
      <defs>
        <linearGradient id="divider-fade" x1="1" y1="0" x2="0" y2="1">
          <stop offset="0" stop-color="#111" stop-opacity="0.15"/>
          <stop offset="0.5" stop-color="#111" stop-opacity="1"/>
          <stop offset="1" stop-color="#111" stop-opacity="0.15"/>
        </linearGradient>
      </defs>
      <line x1="56" y1="4" x2="4" y2="146" stroke="url(#divider-fade)" stroke-width="2"/>
    </svg>
    <div class="reg-no">Business Reg No: 48210957K</div>

    <div class="contact">
      <div class="contact-name">Dev Lunor</div>
      <ul class="contact-list">
        <li>
          <svg viewBox="0 0 24 24" aria-hidden="true"><path fill="#111" d="M6.6 10.8a15 15 0 0 0 6.6 6.6l2.2-2.2c.3-.3.7-.4 1-.2 1.1.4 2.3.6 3.6.6.6 0 1 .4 1 1V20c0 .6-.4 1-1 1A17 17 0 0 1 3 4c0-.6.4-1 1-1h3.5c.6 0 1 .4 1 1 0 1.3.2 2.5.6 3.6.1.3 0 .7-.2 1z"/></svg>
          <span>+65 81749026</span>
        </li>
        <li>
          <svg viewBox="0 0 24 24" aria-hidden="true"><rect x="2" y="5" width="20" height="14" rx="1" fill="#111"/><path d="M3 6l9 7 9-7" stroke="#fff" stroke-width="1.6" fill="none"/></svg>
          <span>jun@tamkeza.example</span>
        </li>
        <li>
          <svg viewBox="0 0 24 24" aria-hidden="true"><circle cx="12" cy="12" r="10" fill="none" stroke="#111" stroke-width="2"/><ellipse cx="12" cy="12" rx="4" ry="10" fill="none" stroke="#111" stroke-width="1.6"/><line x1="2" y1="12" x2="22" y2="12" stroke="#111" stroke-width="1.6"/></svg>
          <span>www.tamkeza.example</span>
        </li>
      </ul>
    </div>
  </section>
</main>
</body>
</html>
```